Amber Reed Properties, which offers a selection of prime properties (villas

A website that contains: Idea, benefits, destinations (villas), offers, about us, contact, newsletter, social media, blog, look at the attachment, even if it is in German. The idea is that I can easily add new pages, if necessary, with the design you make. Later on we want to add a reservation system, so you can book your villa through the internet. Besides, there is a concierge service available, which organizes everything for the customer, owner, from villa to restaurant, limo service, ... & benefits and emotions through nice pictures / videos, they should be convinced to invest.

Target Market(s)

Investors (golfer and non-golfer) which have 300'000 to invest in a kind of real-estate investing club

Number of Pages Required

5+ page

Font styles to use
Sans Serif

Requirements
Must have
• It must be for wordpress, must have an exclusive touch, high quality, with nice pictures of golf courses. The Logo is gold so it has to match with gold, the font is segan or segoe semilight or similar, sans serif
Nice to have
• may be as well as the possibility to include videos of the different destinations and houses

```html
<!DOCTYPE html>
<html lang="de">
<head>
<meta charset="utf-8">
<title>Amber Reed Properties</title>
<link href="https://fonts.googleapis.com/css2?family=Montserrat:wght@300;400;500;600&display=swap" rel="stylesheet">
<style>
:root{
  --black:#000;
  --gold:#eba812;
  --white:#f2f2f2;
  --bar:#1b1b1b;
  --track:#2a2a2a;
  --night:#050403;
  --amber-glow:#8a6420;
  --amber-light:#f2b640;
}
*{margin:0;padding:0;box-sizing:border-box}
html,body{width:1200px;height:2335px;overflow:hidden;background:var(--black)}
body{position:relative;font-family:"Montserrat",sans-serif;color:var(--white)}
.abs{position:absolute}

/* header */
.site-header{left:0;top:0;width:1200px;height:104px}
.nav-link{position:absolute;top:58px;font-size:11.5px;font-weight:400;color:var(--gold);letter-spacing:.2px;text-transform:uppercase;white-space:nowrap}
.brand{position:absolute;left:500px;top:24px;width:200px;text-align:center}
.brand-mark{display:block;width:16px;height:16px;background:var(--gold);margin:0 auto 14px}
.brand-name{display:block;font-size:11px;line-height:14px;color:var(--gold);text-transform:uppercase;white-space:nowrap}

/* hero */
.hero{left:0;top:104px;width:1200px;height:672px;
  background:linear-gradient(180deg,#2f6fc2 0%,#6fa6dc 28%,#b9cfe0 38%,#6f8f3a 45%,#4f8a22 60%,#5fa52a 80%,#3e7a18 100%)}
.hero-title{left:0;top:178px;width:1200px;text-align:center;text-transform:uppercase}
.hero-title .line1{font-size:24px;line-height:30px;font-weight:400;color:#0d1a2a}
.hero-title .line2{display:flex;align-items:center;justify-content:center;gap:10px;font-size:22px;line-height:26px;font-weight:600;color:#0d1a2a}
.hero-title .rule{width:108px;height:3px;background:var(--gold)}

.progress{left:240px;top:797px;width:722px;height:3px;background:var(--track)}
.progress-fill{left:12px;top:0;width:384px;height:3px;background:var(--gold)}

/* idea */
.idea-photo-left{left:0;top:827px;width:386px;height:486px;
  background:linear-gradient(180deg,#4c86d6 0%,#b8d0ea 25%,#3d7a2a 38%,#5a9c34 60%,#d9c9a2 78%,#4f8e26 100%)}
.idea-photo-right{left:813px;top:827px;width:387px;height:486px;
  background:linear-gradient(180deg,#2f6bd0 0%,#8db6ea 28%,#cfc2ad 45%,#bfae98 70%,#8a8c7a 85%,#7f9a52 100%)}
.idea-text{left:386px;top:827px;width:427px;height:486px;text-align:center}
.section-title{font-size:37px;line-height:44px;font-weight:300;color:var(--gold);text-transform:uppercase}
.idea-text .section-title{margin-top:106px}
.idea-body{margin:48px auto 0;width:385px;font-size:11px;line-height:17.5px;font-weight:300;color:var(--white)}

/* offer */
.offer{left:0;top:1388px;width:1200px;text-align:center}
.offer-body{margin:50px auto 0;width:700px;font-size:11px;line-height:17px;font-weight:300;color:var(--white)}
.city-photo{left:0;top:1630px;width:1200px;height:250px;
  background:
    radial-gradient(ellipse 18% 30% at 62% 60%,rgba(242,182,64,.55) 0%,rgba(242,182,64,0) 100%),
    radial-gradient(ellipse 22% 28% at 25% 42%,rgba(242,182,64,.45) 0%,rgba(242,182,64,0) 100%),
    radial-gradient(ellipse 14% 22% at 92% 30%,rgba(242,182,64,.4) 0%,rgba(242,182,64,0) 100%),
    linear-gradient(180deg,var(--night) 0%,#1a1207 14%,var(--amber-glow) 24%,#3d2b0c 40%,#5a4114 55%,#2a1d08 72%,#0d0903 88%,var(--night) 100%)}

/* footer */
.footer-brand{left:500px;top:2052px;width:200px;text-align:center}
.footer-brand .brand-mark{margin-bottom:16px}
.footer-nav .nav-link{top:2132px}
.contact{left:0;top:2170px;width:1200px;text-align:center;font-size:11.5px;line-height:17px;font-weight:300;color:var(--white);font-style:normal}
.social{left:510px;top:2236px;display:flex;gap:16px}
.social-tile{width:23px;height:23px;background:var(--gold);border-radius:3px;display:flex;align-items:center;justify-content:center}
.social-dot{width:9px;height:9px;border-radius:50%;background:var(--black)}
.legal{left:0;top:2287px;width:1200px;height:26px;background:var(--bar);text-align:center;font-size:11px;line-height:26px;color:var(--gold);text-transform:uppercase}
</style>
</head>
<body>

<header class="abs site-header">
  <nav>
    <span class="nav-link" style="left:170px">Idea</span>
    <span class="nav-link" style="left:232px">Benefits</span>
    <span class="nav-link" style="left:323px">Destinations (Villas)</span>
    <span class="nav-link" style="left:744px">Offers</span>
    <span class="nav-link" style="left:824px">About us</span>
    <span class="nav-link" style="left:921px">Contact us</span>
  </nav>
  <div class="brand"><span class="brand-mark"></span><span class="brand-name">Amber Reed Properties</span></div>
</header>

<section class="abs hero" role="img" aria-label="Sunny golf course with bunkers, olive trees and green hills under a blue sky"></section>
<div class="abs hero-title">
  <div class="line1">A selection of prestige golf homes</div>
  <div class="line2"><span class="rule"></span>To invest and enjoy<span class="rule"></span></div>
</div>
<div class="abs progress"><div class="abs progress-fill"></div></div>

<div class="abs idea-photo-left" role="img" aria-label="Golf green with sand bunker and trees under a cloudy blue sky"></div>
<section class="abs idea-text">
  <h2 class="section-title">Unsere Idee</h2>
  <p class="idea-body">Wir bringen Immobilien-Investment, Golf &amp; Lifestyle zusammen<br>Die Idee folgt einem Bedürfnis nach Ferien, Abwechslung und Genuss auf höchstem Niveau und zu attraktiven Konditionen<br>Das Konzept basiert auf vielen Gesprächen und ist unter Mithilfe diverser Experten aus den verschiedensten Bereichen entwickelt worden. Immobilien in Golfresorts werden von Golfern wie Nicht-Golfern geschätzt. Die Gründe dafür sind:<br>Ruhe<br>Gepflegte Parklandschaft<br>Sicherheit<br>Resort Infrastruktur &amp; -Services<br>Werterhaltung</p>
</section>
<div class="abs idea-photo-right" role="img" aria-label="Large family villa with garages under a blue sky"></div>

<section class="abs offer">
  <h2 class="section-title">Unser Angebot</h2>
  <p class="offer-body">Wir bieten Privatpersonen und Firmen Fondsanteile der Amber Reed Properties an. Mit diesen werden Sie Miteigentümer eines weltweit gestreuten Portfolios von exklusiven und stylischen Villen/Apartments, in World Class Golfresorts. Sie können in diesen, mit Familie und Freunden, einige unvergessliche Ferienwochen geniessen, Golf spielen und die Resortangebote/-services nutzen. Wir vermieten die restlichen Wochen bestmöglich auf dem Markt, zu maximal erzielbaren Preisen, was Ihnen wiederum zu Gute kommt. Sie profitieren von einer Wertsteigerung des Portfolios.</p>
</section>
<div class="abs city-photo" role="img" aria-label="Old town panorama at night with warm golden street lights"></div>

<footer>
  <div class="abs footer-brand"><span class="brand-mark"></span><span class="brand-name">Amber Reed Properties</span></div>
  <nav class="footer-nav">
    <span class="nav-link" style="left:310px">Idea</span>
    <span class="nav-link" style="left:372px">Benefits</span>
    <span class="nav-link" style="left:462px">Destinations (Villas)</span>
    <span class="nav-link" style="left:633px">Offers</span>
    <span class="nav-link" style="left:714px">About us</span>
    <span class="nav-link" style="left:811px">Contact us</span>
  </nav>
  <address class="abs contact">C/O Fairway Holding Partners GmbH Seeblickweg 14 CH-8700 Lindenau am See Zurich / Switzerland<br>+41 44 000 12 34, +41 76 000 56 78<br>info@fairwayholding.example</address>
  <div class="abs social" aria-label="Social media links">
    <span class="social-tile"><span class="social-dot"></span></span>
    <span class="social-tile"><span class="social-dot"></span></span>
    <span class="social-tile"><span class="social-dot"></span></span>
    <span class="social-tile"><span class="social-dot"></span></span>
    <span class="social-tile"><span class="social-dot"></span></span>
  </div>
  <div class="abs legal">All rights reserved</div>
</footer>

</body>
</html>
```